Detail Shop Business card design

i need a business card design for my new detailing company called 'Brenner's Detail Shop'. i want an all black and white design . simple, direct and to the point. i want the designer to choose a fitting font to match the logothe front should have logo, address, phone and email and the back side should have a slogan and text indicating that we offer services on anything including cars, trucks, motorcycles and RVs. slogan will read "we take pride in your ride"
maybe also very small on the back side the IG icon with Brenners_Detail_Shop

phone 482.615.7734
address 7384 E Harlow Ave
Spokane WA 99342
email: BrennersDetail@quorvail.com

Target Market(s)

all ages , auto enthusiasts

Industry/Entity Type

Automotive

Contact Information for Business Card

the front should have logo, address, phone and email and the back side should have a slogan and text indicating that we offer services on anything including cars, trucks, motorcycles and RVs. slogan will read "we take pride in your ride"

phone 482.615.7734
address 7384 E Harlow Ave
Spokane WA 99342

Colors
000000
ffffff

Requirements
Must have
• bold font and very simple design with good spacing
Nice to have
• anything creative from the designer indicating we service any types of vehicles
Should not have
• any colors ,

```html
<!DOCTYPE html>
<html lang="en">
<head>
<meta charset="utf-8">
<title>Brenner's Detail Shop – Business Card</title>
<link rel="stylesheet" href="https://fonts.googleapis.com/css2?family=Arvo:wght@400;700&family=Lato:wght@400;700&display=swap">
<style>
  :root {
    --ink: #000000;
    --paper: #ffffff;
    --stage: #3b3b3d;
    --rule: #555555;
  }
  * { box-sizing: border-box; margin: 0; padding: 0; }
  html, body { width: 1200px; height: 1200px; overflow: hidden; }
  body { background: var(--stage); position: relative; font-family: "Lato", sans-serif; }

  .card {
    position: absolute;
    left: 120px;
    width: 960px;
    height: 548px;
    border-radius: 48px;
    overflow: hidden;
  }

  /* Back side */
  .card-back { top: 40px; background: var(--ink); color: var(--paper); text-align: center; }
  .slogan {
    font-family: "Arvo", serif; font-weight: 700; font-size: 50px;
    margin-top: 62px; letter-spacing: 1px;
  }
  .brand-mark {
    display: inline-flex; align-items: center; gap: 12px;
    margin-top: 22px; font-family: "Arvo", serif; font-weight: 700; font-size: 24px;
  }
  .brand-dot { width: 18px; height: 18px; border-radius: 50%; background: currentColor; }
  .services-pill {
    display: inline-block; margin-top: 24px;
    background: var(--paper); color: var(--ink);
    font-size: 28px; padding: 6px 26px; border-radius: 30px;
  }
  .service-list {
    display: flex; justify-content: center; gap: 56px; margin-top: 30px;
  }
  .service { display: flex; flex-direction: column; align-items: center; gap: 12px; }
  .service-icon {
    width: 64px; height: 64px; border-radius: 50%;
    border: 2px dotted var(--rule); display: flex; align-items: center; justify-content: center;
  }
  .service-icon svg { width: 40px; height: 28px; fill: var(--paper); }
  .service-name { font-family: "Arvo", serif; font-weight: 700; font-size: 34px; }
  .social {
    display: inline-flex; align-items: center; gap: 10px;
    margin-top: 28px; padding-top: 12px; border-top: 1px solid var(--rule);
    font-size: 20px; font-weight: 700;
  }
  .social-dot { width: 18px; height: 18px; border: 2px solid var(--paper); border-radius: 4px; }

  /* Front side */
  .card-front { top: 612px; background: var(--paper); color: var(--ink); }
  .front-brand {
    position: absolute; left: 70px; top: 150px; width: 440px;
    display: flex; align-items: center; gap: 22px;
    font-family: "Arvo", serif; font-weight: 700; font-size: 50px; line-height: 1.15;
  }
  .front-brand .brand-dot { width: 56px; height: 56px; flex: none; }
  .divider {
    position: absolute; left: 560px; top: 70px; width: 2px; height: 360px; background: var(--ink);
  }
  .divider-tab {
    position: absolute; left: 556px; top: 470px; width: 16px; height: 78px; background: var(--ink);
  }
  .contact {
    position: absolute; left: 600px; top: 170px;
    font-size: 26px; line-height: 1.45;
  }
  .contact .label { font-family: "Arvo", serif; font-weight: 700; display: inline-block; width: 96px; }
</style>
</head>
<body>

<section class="card card-back" aria-label="Card back">
  <h1 class="slogan">We take pride in your ride!</h1>
  <div class="brand-mark"><span class="brand-dot"></span>Brenner's Detail Shop</div>
  <div><span class="services-pill">Our services include:</span></div>
  <ul class="service-list" style="list-style:none">
    <li class="service">
      <span class="service-icon"><svg viewBox="0 0 40 28"><path d="M4 18 L8 10 H30 L36 18 V22 H4 Z"/><circle cx="11" cy="23" r="4"/><circle cx="29" cy="23" r="4"/></svg></span>
      <span class="service-name">Cars</span>
    </li>
    <li class="service">
      <span class="service-icon"><svg viewBox="0 0 40 28"><rect x="2" y="4" width="22" height="16"/><path d="M25 9 H32 L38 15 V20 H25 Z"/><circle cx="10" cy="22" r="4"/><circle cx="31" cy="22" r="4"/></svg></span>
      <span class="service-name">Truck</span>
    </li>
    <li class="service">
      <span class="service-icon"><svg viewBox="0 0 40 28"><circle cx="8" cy="20" r="6"/><circle cx="32" cy="20" r="6"/><path d="M8 18 L16 10 H26 L32 18 H28 L24 14 H18 L12 20 Z"/></svg></span>
      <span class="service-name">Motorcycles</span>
    </li>
    <li class="service">
      <span class="service-icon"><svg viewBox="0 0 40 28"><rect x="2" y="4" width="32" height="16" rx="2"/><path d="M34 10 L38 14 V20 H34 Z"/><circle cx="10" cy="22" r="4"/><circle cx="28" cy="22" r="4"/></svg></span>
      <span class="service-name">RVs</span>
    </li>
  </ul>
  <div class="social"><span class="social-dot"></span>Brenners_Detail_Shop</div>
</section>

<section class="card card-front" aria-label="Card front">
  <div class="front-brand"><span class="brand-dot"></span><span>Brenner's<br>Detail Shop</span></div>
  <div class="divider"></div>
  <div class="divider-tab"></div>
  <address class="contact" style="font-style:normal">
    <div>7384 E Harlow Ave</div>
    <div>Spokane WA 99342</div>
    <div><span class="label">Mob:</span>482.615.7734</div>
    <div><span class="label">Email:</span>BrennersDetail@quorvail.com</div>
  </address>
</section>

</body>
</html>
```